VELMIT Business Card

VELMIT (www.velmitpools.example) is a veteran in the swimming pool maintenance and repair business..we have served our clients for 15 years and have a research chemist, an electrician, a plumber and a pool building contractor (in part) on staff...We want to provide a business card that has a dual purpose, that people want to keep around, that leaves people speechless in the sense that they understand the mission of and the experience level of the TEAM at VELMIT.

Target Market(s)

persons who enjoy swimming and make it a priority to swim

Industry/Entity Type

Building

Font styles to use
Serif
Sans Serif

Colors
85acd3
3176b5
95b6d8
3276b5
0355a3
0555a3
0255a3
0455a3
85abd2

Requirements
Must have
• name, title, address, email, text
Nice to have
• a die cut shape
Should not have
• cartoons, pictures of pools

```html
<!DOCTYPE html>
<html lang="en">
<head>
<meta charset="utf-8">
<title>VELMIT Business Card</title>
<link rel="stylesheet" href="https://fonts.googleapis.com/css2?family=Open+Sans:wght@400;600;700;800&display=swap">
<style>
  :root {
    --brand-blue: #3176b5;
    --deep-blue: #0355a3;
    --sky-blue: #85acd3;
    --mist-blue: #95b6d8;
    --aqua: #1aa3d9;
    --aqua-dark: #0e86c2;
    --ink: #1f5f9c;
    --paper: #ffffff;
    --backdrop: #eef1f5;
  }
  * { box-sizing: border-box; margin: 0; padding: 0; }
  html, body { width: 1200px; height: 667px; overflow: hidden; }
  body {
    background: var(--backdrop);
    font-family: "Open Sans", sans-serif;
    position: relative;
  }
  .card {
    position: absolute;
    top: 186px;
    width: 500px;
    height: 295px;
    border-radius: 60px 0 60px 0;
    overflow: hidden;
    box-shadow: 0 6px 18px rgba(20, 50, 90, 0.18);
  }
  /* Front */
  .card-front { left: 70px; background: var(--paper); }
  .wordmark {
    position: absolute; left: 44px; top: 38px;
    display: flex; align-items: center; gap: 12px;
  }
  .wordmark-square { width: 22px; height: 22px; background: var(--brand-blue); }
  .wordmark-name {
    font-size: 50px; font-weight: 600; color: var(--brand-blue);
    letter-spacing: 1px; line-height: 1;
  }
  .tagline {
    position: absolute; left: 44px; top: 102px;
    font-size: 13px; letter-spacing: 2px; color: var(--aqua);
  }
  .person { position: absolute; right: 34px; top: 60px; text-align: right; }
  .person-name { font-size: 17px; font-weight: 600; color: var(--brand-blue); }
  .person-title { font-size: 12px; font-weight: 600; color: var(--deep-blue); }
  .contact-list {
    position: absolute; left: 44px; top: 178px; list-style: none;
    font-size: 14.5px; color: var(--ink); line-height: 21px;
  }
  .contact-list li { display: flex; align-items: center; gap: 8px; }
  .contact-icon { width: 14px; height: 14px; flex: none; }
  /* Back */
  .card-back {
    left: 630px;
    background: linear-gradient(160deg, var(--aqua) 0%, var(--aqua-dark) 100%);
  }
  .bubble-field {
    position: absolute; right: 0; top: 60px; width: 260px; height: 235px;
    background: radial-gradient(ellipse at 60% 50%, rgba(255,255,255,0.22), rgba(255,255,255,0) 70%);
  }
  .senses-heading {
    position: absolute; left: 150px; top: 26px; color: var(--paper);
  }
  .senses-heading h2 { font-size: 24px; font-weight: 800; letter-spacing: 0.5px; line-height: 1.05; }
  .senses-heading p { font-size: 12px; font-weight: 600; letter-spacing: 1px; opacity: 0.8; }
  .senses-list { position: absolute; left: 34px; top: 96px; list-style: none; }
  .sense { display: flex; align-items: center; gap: 12px; margin-bottom: 10px; }
  .sense-icon {
    width: 34px; height: 34px; border-radius: 50%; background: var(--paper);
    display: flex; align-items: center; justify-content: center; flex: none;
  }
  .sense-label { font-size: 10px; letter-spacing: 1px; color: rgba(255,255,255,0.7); }
  .sense-answer { font-size: 13px; font-weight: 700; color: var(--paper); letter-spacing: 0.3px; }
</style>
</head>
<body>

  <section class="card card-front" aria-label="Card front">
    <div class="wordmark">
      <span class="wordmark-square"></span>
      <span class="wordmark-name">VELMIT</span>
    </div>
    <p class="tagline">CLEAR WATER...EVERY DAY</p>

    <div class="person">
      <p class="person-name">Dana Hollis</p>
      <p class="person-title">Manager</p>
    </div>

    <ul class="contact-list">
      <li>
        <svg class="contact-icon" viewBox="0 0 16 16"><path d="M3 1l3 3-2 2c1 2 3 4 5 5l2-2 3 3-2 3C7 15 1 9 1 3z" fill="#3176b5"/></svg>
        +44 (0) 20 5550 0142
      </li>
      <li>
        <svg class="contact-icon" viewBox="0 0 16 16"><rect x="1" y="3" width="14" height="10" fill="#3176b5"/><path d="M1 3l7 6 7-6" stroke="#fff" stroke-width="1.4" fill="none"/></svg>
        dana@velmitpools.example
      </li>
      <li>
        <svg class="contact-icon" viewBox="0 0 16 16"><circle cx="8" cy="8" r="6.5" fill="none" stroke="#3176b5" stroke-width="1.5"/><path d="M1.5 8h13M8 1.5c-3 3-3 10 0 13M8 1.5c3 3 3 10 0 13" stroke="#3176b5" stroke-width="1.2" fill="none"/></svg>
        www.velmitpools.example
      </li>
      <li>
        <svg class="contact-icon" viewBox="0 0 16 16"><path d="M8 1l7 7h-2v7H9v-4H7v4H3V8H1z" fill="#3176b5"/></svg>
        14 Harbour Lane, Kestwick, KW4 2PL
      </li>
    </ul>
  </section>

  <section class="card card-back" aria-label="Card back">
    <div class="bubble-field" role="img" aria-label="Soft pattern of pale water bubbles"></div>

    <div class="senses-heading">
      <h2>USE YOUR SENSES</h2>
      <p>AT THE POOL</p>
    </div>

    <ul class="senses-list">
      <li class="sense">
        <span class="sense-icon"><svg width="20" height="12" viewBox="0 0 20 12"><path d="M1 6c5-7 13-7 18 0-5 7-13 7-18 0z" fill="none" stroke="#0e86c2" stroke-width="1.6"/><circle cx="10" cy="6" r="2.6" fill="#0e86c2"/></svg></span>
        <div><p class="sense-label">WATER SHOULD LOOK</p><p class="sense-answer">CLEAN, CLEAR AND BLUE</p></div>
      </li>
      <li class="sense">
        <span class="sense-icon"><svg width="16" height="18" viewBox="0 0 16 18"><path d="M4 17V7M4 8V3a1.5 1.5 0 013 0v5M7 7V2a1.5 1.5 0 013 0v6M10 7V3a1.5 1.5 0 013 0v9c0 3-2 5-5 5H6" fill="none" stroke="#0e86c2" stroke-width="1.6"/></svg></span>
        <div><p class="sense-label">SURFACES SHOULD FEEL</p><p class="sense-answer">SMOOTH AND CLEAN</p></div>
      </li>
      <li class="sense">
        <span class="sense-icon"><svg width="14" height="18" viewBox="0 0 14 18"><path d="M7 1c0 6-5 8-5 12a3 3 0 005 2 3 3 0 005-2" fill="none" stroke="#0e86c2" stroke-width="1.6"/></svg></span>
        <div><p class="sense-label">THE AIR HAS</p><p class="sense-answer">NO STRONG ODORS</p></div>
      </li>
      <li class="sense">
        <span class="sense-icon"><svg width="14" height="18" viewBox="0 0 14 18"><path d="M3 7a5 5 0 0110 0c0 4-4 4-4 8a2.5 2.5 0 01-5 0" fill="none" stroke="#0e86c2" stroke-width="1.6"/></svg></span>
        <div><p class="sense-label">LISTEN FOR HUMMING</p><p class="sense-answer">CLEANING EQUIPMENT</p></div>
      </li>
    </ul>
  </section>

</body>
</html>
```